Service Plan Sales Flyer

The Watchpost Depot (www.kelvamart.com) is a commercial security integrator that installs security cameras, access control, intrusion, two-way radios and perimeter security. We require a one page flyer for our service plan for new and existing customers. The price of the service plan is $299/yr and includes the following;
1. Discounted service rate of $118/hr
2. Free remote support ($85/hr without a plan)
3. Free remote training
4. Priority support

Please review our brochure attached and create a one page sales flyer with the end goal of having the client sign up for our annual service plan . The plan will automatically renew every year. Email sales@kelvamart.com.

Target Market(s)

commercial industrial clients - no residential

Industry/Entity Type

review our website at www.kelvamart.com

Colors
0054AA
0677BA
7BADD7
CADEEF
E8F1F8
EE7325
F08F49
F5BC92
FAE3D3
FDF4ED

Requirements
Must have
• call to action
Should not have
• too many colors

```html
<!DOCTYPE html>
<html lang="en">
<head>
<meta charset="utf-8">
<title>The Watchpost Depot – Annual Service Plan Flyer</title>
<link rel="stylesheet" href="https://fonts.googleapis.com/css2?family=Fira+Sans+Extra+Condensed:wght@600;700&family=Lato:wght@400;700;900&display=swap">
<style>
  :root {
    --navy: #1b2f5c;
    --navy-deep: #16284f;
    --orange: #ee5a2e;
    --blue: #1f6bc0;
    --blue-light: #4f93d9;
    --white: #ffffff;
    --page: #eeeeee;
    --head: "Fira Sans Extra Condensed", "Arial Narrow", sans-serif;
    --body: "Lato", Arial, sans-serif;
  }
  * { box-sizing: border-box; margin: 0; padding: 0; }
  html, body { width: 1200px; height: 1200px; overflow: hidden; background: var(--page); }
  .canvas { position: relative; width: 1200px; height: 1200px; overflow: hidden; }

  .flyer {
    position: absolute; left: 204px; top: 40px;
    width: 586px; height: 830px;
    transform: scale(1.35); transform-origin: top left;
    background: var(--white); overflow: hidden;
    font-family: var(--body); color: var(--navy);
  }
  .flyer-shapes { position: absolute; inset: 0; width: 586px; height: 830px; }
  .abs { position: absolute; }

  /* brand */
  .brand { left: 16px; top: 22px; display: flex; align-items: center; gap: 10px; }
  .brand-mark { width: 16px; height: 16px; background: var(--navy); }
  .brand-name { font-family: var(--head); font-weight: 700; font-size: 27px; color: var(--navy); text-transform: uppercase; letter-spacing: .2px; }

  /* right column headline */
  .trust { left: 392px; top: 22px; width: 196px; text-align: center; font-family: var(--head); font-weight: 700; font-size: 31px; line-height: 27px; }
  .trust .accent { color: var(--orange); }

  .products-title { left: 378px; top: 188px; width: 208px; height: 48px; line-height: 48px; text-align: center; color: var(--white); font-weight: 900; font-size: 17px; letter-spacing: 4px; }
  .products { left: 388px; top: 268px; list-style: none; }
  .product { display: flex; align-items: center; height: 36px; margin-bottom: 17.5px; }
  .product-icon { width: 36px; height: 36px; flex: none; }
  .product-text { margin-left: 14px; color: var(--white); font-size: 13.5px; line-height: 17px; letter-spacing: .2px; }
  .product-text b { display: block; font-weight: 900; }

  /* service plan */
  .plan-title { left: 22px; top: 398px; font-family: var(--head); font-weight: 700; font-size: 37px; line-height: 38px; color: var(--white); }
  .price { left: 236px; top: 338px; width: 94px; height: 94px; border-radius: 50%; background: var(--white); border: 3px solid var(--navy); text-align: center; color: var(--navy); padding-top: 18px; }
  .price-amount { display: block; font-family: var(--head); font-weight: 700; font-size: 33px; line-height: 32px; }
  .price-unit { display: block; font-weight: 700; font-size: 14px; line-height: 16px; }
  .renew { left: 228px; top: 438px; width: 110px; text-align: center; color: var(--white); font-size: 10.5px; line-height: 14px; }

  .includes { left: 28px; top: 481px; height: 29px; line-height: 29px; color: var(--white); font-weight: 900; font-size: 16px; letter-spacing: 4px; }
  .benefits { left: 22px; top: 530px; width: 300px; list-style: none; font-weight: 700; font-size: 14.5px; line-height: 18px; color: var(--navy); }
  .benefits li { display: flex; margin-bottom: 11px; }
  .benefits .num { width: 20px; flex: none; }

  .tagline { left: 0; top: 698px; width: 333px; height: 28px; line-height: 28px; text-align: center; color: var(--white); font-weight: 900; font-size: 15.5px; letter-spacing: .4px; }

  .services { left: 0; top: 738px; width: 333px; height: 92px; }
  .service { position: absolute; display: flex; align-items: center; gap: 14px; color: var(--white); font-size: 11px; letter-spacing: .3px; }
  .service svg { width: 24px; height: 24px; flex: none; }

  /* call to action */
  .cta { left: 378px; top: 506px; width: 208px; text-align: center; font-family: var(--head); font-weight: 700; line-height: 28px; }
  .cta-lead { display: block; color: var(--orange); font-size: 35px; line-height: 33px; }
  .cta-rest { display: block; color: var(--navy); font-size: 28px; }
  .signup { left: 378px; top: 607px; width: 208px; text-align: center; color: var(--white); font-weight: 700; font-size: 14px; line-height: 18px; }
  .phone { left: 362px; top: 668px; width: 224px; height: 58px; display: flex; align-items: center; justify-content: center; gap: 6px; color: var(--white); font-family: var(--head); font-weight: 700; font-size: 29px; }
  .phone svg { width: 22px; height: 22px; }
  .address { left: 370px; top: 738px; font-weight: 700; font-size: 11.5px; line-height: 14.5px; color: var(--navy); }
  .website { left: 370px; top: 798px; font-weight: 900; font-size: 19px; color: var(--navy); }
</style>
</head>
<body>
<div class="canvas">
  <div class="flyer">
    <svg class="flyer-shapes" viewBox="0 0 586 830" aria-hidden="true">
      <defs>
        <linearGradient id="photoTone" x1="0" y1="0" x2="1" y2="1">
          <stop offset="0" stop-color="#2a7fd0"/>
          <stop offset="1" stop-color="#1d62b4"/>
        </linearGradient>
      </defs>
      <!-- top-left photo field -->
      <polygon points="0,0 392,0 378,393 0,393" fill="url(#photoTone)"/>
      <polygon points="346,0 392,0 378,393 332,393" fill="var(--navy-deep)"/>
      <!-- logo plate -->
      <polygon points="0,0 318,0 308,73 0,73" fill="var(--white)"/>
      <!-- right column shapes -->
      <polygon points="384,188 586,188 586,236 382,236" fill="var(--orange)"/>
      <polygon points="382,236 586,236 586,496 372,496" fill="var(--navy)"/>
      <!-- service plan band -->
      <polygon points="0,393 380,393 376,478 0,478" fill="var(--orange)"/>
      <polygon points="0,481 220,481 214,510 0,510" fill="var(--navy)"/>
      <!-- tagline & services -->
      <rect x="0" y="698" width="333" height="28" fill="var(--orange)"/>
      <rect x="0" y="738" width="333" height="92" fill="var(--navy)"/>
      <!-- CTA bands -->
      <polygon points="372,603 586,603 586,666 368,666" fill="var(--blue)"/>
      <polygon points="366,668 586,668 586,726 362,726" fill="var(--orange)"/>
    </svg>

    <div class="abs" role="img" aria-label="Product photo: office door, monitor showing camera footage, dome and bullet security cameras on a blue building backdrop" style="left:0;top:73px;width:336px;height:320px;"></div>

    <div class="abs brand">
      <span class="brand-mark"></span>
      <span class="brand-name">The Watchpost Depot</span>
    </div>

    <h2 class="abs trust">
      <span class="accent">CANADA'S<br>MOST<br>TRUSTED</span><br>FOR<br>20+YEARS
    </h2>

    <div class="abs products-title">PRODUCTS</div>
    <ul class="abs products">
      <li class="product">
        <svg class="product-icon" viewBox="0 0 36 36"><circle cx="18" cy="18" r="16" fill="var(--orange)" stroke="#fff" stroke-width="2"/><g fill="none" stroke="#fff" stroke-width="1.6"><rect x="11" y="13" width="14" height="7" rx="1" transform="rotate(18 18 16)"/><path d="M12 12v14M12 24h4"/></g></svg>
        <span class="product-text">SECURITY CAMERA<b>SYSTEM</b></span>
      </li>
      <li class="product">
        <svg class="product-icon" viewBox="0 0 36 36"><circle cx="18" cy="18" r="16" fill="var(--orange)" stroke="#fff" stroke-width="2"/><g fill="none" stroke="#fff" stroke-width="1.5"><rect x="11" y="9" width="14" height="18" rx="1.5"/><rect x="13.5" y="11.5" width="9" height="4"/></g><g fill="#fff"><rect x="13.5" y="18" width="2" height="2"/><rect x="17" y="18" width="2" height="2"/><rect x="20.5" y="18" width="2" height="2"/><rect x="13.5" y="22" width="2" height="2"/><rect x="17" y="22" width="2" height="2"/><rect x="20.5" y="22" width="2" height="2"/></g></svg>
        <span class="product-text">INTRUSION<b>ALARM</b></span>
      </li>
      <li class="product">
        <svg class="product-icon" viewBox="0 0 36 36"><circle cx="18" cy="18" r="16" fill="var(--orange)" stroke="#fff" stroke-width="2"/><g fill="none" stroke="#fff" stroke-width="1.7"><circle cx="14" cy="14" r="4"/><path d="M17 17l9 9M22 22l2-2M24.5 24.5l2-2"/><path d="M10 26l16-16" stroke-width="1.3"/></g></svg>
        <span class="product-text">ACCESS CONTROL<b>&amp; INTERCOM</b></span>
      </li>
      <li class="product">
        <svg class="product-icon" viewBox="0 0 36 36"><circle cx="18" cy="18" r="16" fill="var(--orange)" stroke="#fff" stroke-width="2"/><g fill="none" stroke="#fff" stroke-width="1.4"><path d="M10 26V11M15 26V11M20 26V11M25 26V11M10 15h15M10 22h15M10 11l15 11M25 11L10 22"/></g></svg>
        <span class="product-text">PERIMETER<b>SECURITY</b></span>
      </li>
    </ul>

    <h1 class="abs plan-title">ANNUAL<br>SERVICE PLAN</h1>
    <div class="abs price"><span class="price-amount">$299</span><span class="price-unit">/year</span></div>
    <p class="abs renew">Automatically Renew Every Year</p>

    <div class="abs includes">INCLUDES</div>
    <ol class="abs benefits">
      <li><span class="num">1.</span><span>DISCOUNTED SERVICE RATE<br>OF $118/HR</span></li>
      <li><span class="num">2.</span><span>FREE REMOTE SUPPORT<br>($85/HR WITHOUT A PLAN)</span></li>
      <li><span class="num">3.</span><span>FREE REMOTE TRAINING</span></li>
      <li><span class="num">4.</span><span>PRIORITY SUPPORT</span></li>
    </ol>

    <div class="abs tagline">KNOWLEDGEABLE | RELIABLE | EASY</div>

    <div class="abs services">
      <svg style="position:absolute;left:0;top:0" width="333" height="92" viewBox="0 0 333 92" aria-hidden="true">
        <line x1="157" y1="8" x2="157" y2="84" stroke="#fff" stroke-opacity=".5" stroke-width="1"/>
        <line x1="15" y1="44" x2="147" y2="44" stroke="#fff" stroke-opacity=".5" stroke-width="1"/>
        <line x1="168" y1="44" x2="325" y2="44" stroke="#fff" stroke-opacity=".5" stroke-width="1"/>
      </svg>
      <div class="service" style="left:20px;top:14px;">
        <svg viewBox="0 0 24 24" fill="none" stroke="var(--orange)" stroke-width="1.6"><circle cx="12" cy="8" r="4.5"/><path d="M4 22c0-5 3.5-7 8-7s8 2 8 7z"/></svg>
        <span>CONSULTATION</span>
      </div>
      <div class="service" style="left:172px;top:14px;">
        <svg viewBox="0 0 24 24" fill="none" stroke="var(--orange)" stroke-width="1.8"><path d="M4 4l16 16M20 4L4 20"/><path d="M2 6l4-4M18 22l4-4"/></svg>
        <span>INSTALLATION</span>
      </div>
      <div class="service" style="left:20px;top:52px;">
        <svg viewBox="0 0 24 24" fill="none" stroke="var(--orange)" stroke-width="1.6"><path d="M5 2h10l4 4v16H5z"/><text x="12" y="18" font-family="Lato, sans-serif" font-size="10" font-weight="700" fill="var(--orange)" stroke="none" text-anchor="middle">$</text></svg>
        <span>DESIGN</span>
      </div>
      <div class="service" style="left:172px;top:52px;">
        <svg viewBox="0 0 24 24" fill="none" stroke="var(--orange)" stroke-width="1.8"><path d="M4 14v-2a8 8 0 0 1 16 0v2"/><rect x="3" y="13" width="4" height="6" rx="1"/><rect x="17" y="13" width="4" height="6" rx="1"/><path d="M19 19c0 2-2 3-5 3"/></svg>
        <span>SUPPORT</span>
      </div>
    </div>

    <div class="abs cta">
      <span class="cta-lead">CALL US</span>
      <span class="cta-rest">FOR YOUR<br>FREE QUOTE</span>
    </div>
    <p class="abs signup">AND SIGN UP<br>FOR OUR ANNUAL<br>SECURITY PLAN.</p>
    <div class="abs phone">
      <svg viewBox="0 0 24 24" fill="#fff"><path d="M6.6 10.8a15 15 0 0 0 6.6 6.6l2.2-2.2a1 1 0 0 1 1-.25 11.4 11.4 0 0 0 3.6.57 1 1 0 0 1 1 1V20a1 1 0 0 1-1 1A17 17 0 0 1 3 4a1 1 0 0 1 1-1h3.5a1 1 0 0 1 1 1c0 1.25.2 2.45.57 3.57a1 1 0 0 1-.25 1z"/></svg>
      <span>1-877-555-0142</span>
    </div>
    <address class="abs address" style="font-style:normal;">
      #12, 780 Harrow Bend SE<br>Calgary, AB T2C 0X4<br>403-555-0186<br>403-555-0127
    </address>
    <div class="abs website">www.kelvamart.com</div>
  </div>
</div>
</body>
</html>
```